Harborline Talent Web Site

I would like to change our current website to a better design. www.harborlinetalent.net.
Use the content from the this website.
Updates
The web site is down until 7AM EST on 3/25 for server maintenance. Sorry for the inconvenience.
REMEMBER: I am changing the website to focus on science and technical jobs across all industries. So, if your images focus on only biotech or only DNA or beakers that will not serve Aerospace very well or curcuit board manufacturing. So, either use a montage of images that cover everything or make you images more abstract.
Target Market(s)
We are now staffing for all science and technical jobs. Not just biotech and pharmaceutical.
So, pharmaceutical, biotech, aerospace, alternative energy, research, medical...etc. Anyone with a science or tehcnical background.
Number of Pages Required
5+ pages
Requirements
Must have
- Tag line: "The Science of Recruiting" replaces "A pharmaceutical and bitech search firm"
Pictures and images across more industries.
The job serach page only needs a banner. That page is being worked internally.

```html
<!DOCTYPE html>
<html lang="en">
<head>
<meta charset="utf-8">
<title>Harborline Talent — The Science of Recruiting</title>
<link rel="stylesheet" href="https://fonts.googleapis.com/css2?family=Arimo:wght@400;700&family=Open+Sans:wght@400;600&family=Questrial&display=swap">
<style>
  :root {
    --green: #1f5a2c;
    --green-dark: #17481f;
    --orange: #c3760a;
    --orange-dark: #9c5c04;
    --orange-light: #d88d1e;
    --ink: #1e1e1e;
    --grey-line: #a9a9a9;
    --panel: #f0f0f0;
    --footer-top: #3a3a3a;
    --footer-bottom: #151515;
    --white: #ffffff;
  }
  * { margin: 0; padding: 0; box-sizing: border-box; }
  html, body { width: 1200px; height: 1002px; overflow: hidden; }
  body {
    position: relative;
    background: var(--white);
    font-family: "Open Sans", Verdana, sans-serif;
    color: var(--ink);
  }

  /* Header */
  .site-header {
    position: absolute; left: 0; top: 0; width: 1200px; height: 146px;
    background: linear-gradient(#ffffff 0%, #f3f3f3 60%, #e2e2e2 100%);
  }
  .brand {
    position: absolute; left: 28px; top: 66px;
    display: flex; align-items: center; gap: 12px;
    font-weight: 400; font-size: 31px; letter-spacing: 1px; line-height: 40px;
    color: var(--green-dark); text-transform: uppercase;
  }
  .brand-mark { width: 14px; height: 14px; background: var(--orange); }
  .tagline {
    position: absolute; left: 590px; top: 66px;
    font-weight: 400; font-size: 30px; letter-spacing: 1px; line-height: 40px;
    color: var(--green-dark); text-transform: uppercase;
  }

  /* Navigation */
  .main-nav {
    position: absolute; left: 0; top: 146px; width: 1200px; height: 44px;
    background: linear-gradient(var(--orange-light), var(--orange) 55%, var(--orange-dark));
  }
  .main-nav a {
    position: absolute; top: 0; height: 44px; line-height: 44px;
    font-family: Arimo, Arial, sans-serif; font-weight: 700; font-size: 17px;
    color: var(--white); text-decoration: none;
  }
  .nav-sep {
    position: absolute; top: 5px; width: 1px; height: 34px;
    background: rgba(255, 220, 160, 0.55);
  }

  /* Content panel */
  .content {
    position: absolute; left: 7px; top: 190px; width: 1186px; height: 614px;
    background: var(--white);
    border-left: 2px solid #d6d6d6; border-right: 2px solid #d6d6d6;
    box-shadow: inset 3px 0 4px -2px #cfcfcf, inset -3px 0 4px -2px #cfcfcf;
  }
  .hero-frame {
    position: absolute; left: 36px; top: 218px; width: 751px; height: 310px;
    border: 1px solid var(--grey-line); background: var(--white);
  }
  .hero-image {
    position: absolute; left: 7px; top: 7px; width: 733px; height: 294px;
    background: linear-gradient(100deg, #1f3f8a 0%, #3461b4 35%, #6fa6df 60%, #a9d3f2 80%, #5f9bd8 100%);
  }
  .welcome {
    position: absolute; left: 41px; top: 546px;
    font-family: Questrial, "Century Gothic", sans-serif;
    font-size: 29px; font-weight: 400; color: var(--green);
  }
  .intro {
    position: absolute; left: 41px; top: 596px; width: 700px;
    font-size: 15px; line-height: 19.2px; color: var(--ink);
  }
  .intro p + p { margin-top: 19px; }

  .side-box {
    position: absolute; left: 821px; width: 348px;
    border: 1px solid #c8c8c8;
    background: linear-gradient(#e9e9e9, #ffffff 40%, #f7f7f7);
  }
  .box-title {
    text-align: center; font-family: Arimo, Arial, sans-serif;
    font-weight: 700; font-size: 21px; color: var(--green);
  }
  .box-rule {
    position: absolute; left: 18px; width: 302px; height: 2px; background: var(--grey-line);
  }
  .feature { top: 218px; height: 309px; }
  .feature .box-title { position: absolute; left: 0; right: 0; top: 18px; }
  .feature .box-rule { top: 54px; }
  .feature-text {
    position: absolute; left: 24px; top: 86px; width: 310px;
    font-size: 14.6px; line-height: 21.6px;
  }
  .read-more {
    position: absolute; left: 24px; top: 221px; width: 101px; height: 29px;
    background: var(--orange); border: 1px solid #7e4a02;
    color: var(--white); font-size: 13px; line-height: 27px; text-align: center;
    text-decoration: none;
  }
  .pager {
    position: absolute; left: 0; bottom: 0; width: 100%; height: 44px;
    background: linear-gradient(#0f0f0f, #3d3d3d);
    display: flex; justify-content: center; align-items: center; gap: 11px;
    font-family: Arimo, Arial, sans-serif; font-size: 18px; color: var(--white);
  }
  .pager .bar { font-weight: 700; }

  .job-search { top: 548px; height: 142px; background: var(--panel); }
  .job-search .box-title { position: absolute; left: 0; right: 0; top: 15px; }
  .job-search .box-rule { top: 47px; }
  .search-field {
    position: absolute; left: 21px; top: 77px; width: 305px; height: 35px;
    background: var(--white); border: 1px solid #c4c4c4; display: flex;
  }
  .search-field span {
    flex: 1; padding-left: 13px; line-height: 33px; font-size: 14.5px; color: #8a8a8a;
  }
  .search-button {
    width: 49px; height: 33px; border-left: 2px solid var(--green);
    display: flex; align-items: center; justify-content: center;
  }

  /* Footer */
  .site-footer {
    position: absolute; left: 0; top: 804px; width: 1200px; height: 152px;
    background: linear-gradient(var(--footer-top), var(--footer-bottom));
    color: var(--white);
  }
  .footer-col { position: absolute; top: 26px; width: 305px; }
  .footer-col h3 {
    font-family: Arimo, Arial, sans-serif; font-weight: 700; font-size: 17.5px; line-height: 22px;
  }
  .footer-col p { font-size: 13.5px; line-height: 17px; }
  .footer-divider {
    position: absolute; top: 24px; height: 104px; border-left: 1px dotted #6a6a6a;
  }
  .bottom-bar {
    position: absolute; left: 0; top: 956px; width: 1200px; height: 46px;
    background: linear-gradient(var(--orange-light), var(--orange-dark));
    color: var(--white); font-size: 13.6px; line-height: 46px;
  }
  .copyright { position: absolute; left: 10px; }
  .footer-links { position: absolute; right: 18px; }
  .footer-links a { color: var(--white); text-decoration: none; }
</style>
</head>
<body>
  <header class="site-header">
    <div class="brand"><span class="brand-mark"></span>Harborline Talent</div>
    <div class="tagline">The Science of Recruiting</div>
  </header>

  <nav class="main-nav">
    <a href="#" style="left:39px">Home</a>
    <span class="nav-sep" style="left:120px"></span>
    <a href="#" style="left:136px">About Us</a>
    <span class="nav-sep" style="left:244px"></span>
    <a href="#" style="left:270px">Expertise</a>
    <span class="nav-sep" style="left:370px"></span>
    <a href="#" style="left:401px">Employer Services</a>
    <span class="nav-sep" style="left:580px"></span>
    <a href="#" style="left:605px">Candidate Services</a>
    <span class="nav-sep" style="left:787px"></span>
    <a href="#" style="left:810px">Conact Us</a>
  </nav>

  <main>
    <div class="content"></div>

    <div class="hero-frame">
      <div class="hero-image" role="img" aria-label="Photo of solar panels beside solar-powered street lamps under a blue sky"></div>
    </div>

    <h1 class="welcome">Welcome to Harborline Talent</h1>
    <div class="intro">
      <p>Executive Search, Recruiting and Contract Services Employees are every company's key to success. Harborline Talent is a recruiting and search firm distinctly focused on those industries we know best. We have placed employees at all levels throughout the United States.</p>
      <p>Our continued success and growth are a result of a consistent high level of service with unparalleled commitment to quality and integrity. We are a partner with our clients who rely on our network of candidates within the industry to help them achieve the next level of excellence.</p>
    </div>

    <section class="side-box feature">
      <h2 class="box-title">Alternative Energy Solution</h2>
      <div class="box-rule"></div>
      <p class="feature-text">Lorem Ipsum is simply dummy text of the printing and typesetting industry. Lorem Ipsum has been the industry's standard dummy text ever since the 1500s,</p>
      <a href="#" class="read-more">Read More</a>
      <div class="pager">
        <span>&lt;</span><span>&nbsp;1</span><span class="bar">|</span><span>2</span><span class="bar">|</span><span>3</span><span class="bar">|</span><span>4</span><span class="bar">|</span><span>5</span><span>&gt;</span>
      </div>
    </section>

    <section class="side-box job-search">
      <h2 class="box-title">Search Job Openings</h2>
      <div class="box-rule"></div>
      <div class="search-field">
        <span>Search...</span>
        <div class="search-button">
          <svg width="24" height="24" viewBox="0 0 24 24" aria-hidden="true">
            <circle cx="9" cy="9" r="6.5" fill="#e8eef2" stroke="#555" stroke-width="2"/>
            <line x1="14" y1="14" x2="21" y2="21" stroke="#333" stroke-width="3.5" stroke-linecap="round"/>
          </svg>
        </div>
      </div>
    </section>
  </main>

  <footer class="site-footer">
    <div class="footer-col" style="left:43px">
      <h3>Upcoming Events</h3>
      <p>It is a long established fact that a reader will be distracted by the readable content of a page when looking at its layout.</p>
    </div>
    <div class="footer-divider" style="left:393px"></div>
    <div class="footer-col" style="left:449px">
      <h3>Recent News</h3>
      <p>It is a long established fact that a reader will be distracted by the readable content of a page when looking at its layout.</p>
    </div>
    <div class="footer-divider" style="left:788px"></div>
    <div class="footer-col" style="left:820px; width:360px">
      <h3>Contact Us</h3>
      <p>&nbsp;Daniel Whitcombe<br>&nbsp;Managing Director<br>&nbsp;(410) 555-0147<br>&nbsp;daniel.whitcombe@harborlinetalent.net</p>
    </div>
  </footer>

  <div class="bottom-bar">
    <span class="copyright">Copyright 2005,HarborlineTalent All rights reserved</span>
    <span class="footer-links"><a href="#">Home</a> | <a href="#">About Us</a> | <a href="#">Expertise</a> | <a href="#">Employer Services</a> | <a href="#">Candidate Services</a> | <a href="#">Conact Us</a></span>
  </div>
</body>
</html>
```